MEKO Business Card Design

I have a rough idea of the design / layout of the company business card but need help in finalizing the design and quality.

I'm looking for the card to be stand out, but simple, on the front with clear detail on the back with space for some one to write any other detail they need onto the card. The rough draft includes the crinkled graph paper back ground which I quite like for the front.

I will need the card design completed and ready to print in Australian business card standard sizes. This includes detail on all colors, fonts and type faces used as well as copy of the original for editing (inserting other employee details).

I have included the company logo and a rough draft of the card, including the graphic I would like to use for the back ground on the front, I am not sure that the graphic is any good for printing, not the highest res.

Thanks,

Lyle

```html
<!DOCTYPE html>
<html lang="en">
<head>
<meta charset="utf-8">
<title>MEKO Business Card</title>
<link href="https://fonts.googleapis.com/css2?family=Oswald:wght@500;700&family=Crimson+Text:ital,wght@0,400;1,400&display=swap" rel="stylesheet">
<style>
  :root {
    --stage: #e4e4e2;
    --card-white: #ffffff;
    --ink: #111111;
    --ink-soft: #2a2a2a;
    --paper-light: #f3f3f1;
    --paper-mid: #dcdcda;
    --shadow: rgba(0, 0, 0, 0.18);
  }
  * { box-sizing: border-box; margin: 0; padding: 0; }
  html, body {
    width: 1200px;
    height: 873px;
    overflow: hidden;
    background: var(--stage);
  }
  .stage {
    width: 1200px;
    height: 873px;
    display: flex;
    align-items: center;
    justify-content: center;
    gap: 70px;
  }
  .card {
    position: relative;
    box-shadow: 0 6px 18px var(--shadow);
    overflow: hidden;
  }

  /* Back: contact details, landscape */
  .card-back {
    width: 560px;
    height: 342px;
    background: var(--card-white);
    color: var(--ink);
  }
  .brand-small {
    position: absolute;
    left: 36px;
    top: 30px;
    font-family: "Oswald", sans-serif;
    font-weight: 700;
    font-size: 34px;
    line-height: 1;
    letter-spacing: 1px;
  }
  .identity {
    position: absolute;
    left: 36px;
    top: 92px;
  }
  .person-name {
    font-family: "Oswald", sans-serif;
    font-weight: 700;
    font-size: 21px;
    letter-spacing: 0.5px;
    padding-bottom: 3px;
    border-bottom: 1.5px solid var(--ink);
    display: inline-block;
  }
  .person-role {
    font-family: "Crimson Text", serif;
    font-style: italic;
    font-size: 18px;
    color: var(--ink-soft);
    margin-top: 2px;
  }
  .contact-list {
    position: absolute;
    left: 200px;
    top: 176px;
    list-style: none;
    font-family: "Crimson Text", serif;
    font-size: 15.5px;
    line-height: 1.45;
  }
  .contact-list li {
    display: flex;
    align-items: center;
    gap: 7px;
  }
  .contact-list .icon {
    width: 11px;
    height: 11px;
    flex: none;
  }
  .contact-list .plain { padding-left: 0; }

  /* Front: paper background with brand name, portrait */
  .card-front {
    width: 342px;
    height: 560px;
    background: var(--paper-light);
  }
  .paper-texture {
    position: absolute;
    inset: 0;
    background: radial-gradient(circle at 35% 30%, var(--paper-light), var(--paper-mid));
  }
  .brand-large {
    position: absolute;
    left: 0;
    right: 0;
    top: 150px;
    text-align: center;
    font-family: "Oswald", sans-serif;
    font-weight: 700;
    font-size: 78px;
    line-height: 1;
    letter-spacing: 3px;
    color: var(--ink);
  }
</style>
</head>
<body>
<main class="stage">
  <section class="card card-back" aria-label="Card back with contact details">
    <div class="brand-small">MEKO</div>
    <div class="identity">
      <div class="person-name">LYLEHARLOW</div>
      <div class="person-role">Operations Manager</div>
    </div>
    <ul class="contact-list">
      <li>
        <svg class="icon" viewBox="0 0 12 12"><rect x="0.5" y="2" width="11" height="8" fill="none" stroke="#111" stroke-width="1.2"/><path d="M0.5 2.5 L6 7 L11.5 2.5" fill="none" stroke="#111" stroke-width="1.2"/></svg>
        lharlow@meko.com.au
      </li>
      <li>
        <svg class="icon" viewBox="0 0 12 12"><path d="M3 1 L5 3.5 L4 5 Q5 7.5 7 8 L8.5 7 L11 9 L9.5 11 Q3 10 1 2.5 Z" fill="#111"/></svg>
        9031 5528
      </li>
      <li>
        <svg class="icon" viewBox="0 0 12 12"><rect x="3" y="0.5" width="6" height="11" rx="1" fill="#111"/><rect x="4" y="2" width="4" height="6.5" fill="#fff"/></svg>
        0411 238 904
      </li>
      <li>
        <svg class="icon" viewBox="0 0 12 12"><circle cx="6" cy="6" r="5" fill="none" stroke="#111" stroke-width="1.2"/><ellipse cx="6" cy="6" rx="2.2" ry="5" fill="none" stroke="#111" stroke-width="1"/><path d="M1 6 H11" stroke="#111" stroke-width="1"/></svg>
        www.meko.com.au
      </li>
      <li>
        <svg class="icon" viewBox="0 0 12 12"><path d="M6 11.5 C3 7.5 2 6 2 4.5 A4 4 0 0 1 10 4.5 C10 6 9 7.5 6 11.5 Z" fill="#111"/><circle cx="6" cy="4.5" r="1.5" fill="#fff"/></svg>
        12/46 Wattle Lane Melbourne 3000
      </li>
      <li class="plain">Melbourne / Perth</li>
    </ul>
  </section>

  <section class="card card-front" aria-label="Card front">
    <div class="paper-texture" role="img" aria-label="Crinkled graph paper background"></div>
    <div class="brand-large">MEKO</div>
  </section>
</main>
</body>
</html>
```